New Flyer Design Project Larkspur Panels and Spaces

Real photos will be added but please start with these for layout. Copy will be supplied so you can just leave a text box to start I am open to suggestions. Thank you

Target Market(s)

Builders, Designers, remodelers, consumers

Colors

Designer to choose colors to be used in the design.

Requirements
Must have
• Before and after photos, email, phone, logo, description

```html
<!DOCTYPE html>
<html lang="en">
<head>
<meta charset="utf-8">
<title>Larkspur Panels and Spaces – Flyer</title>
<link href="https://fonts.googleapis.com/css2?family=Montserrat:ital,wght@0,400;0,600;0,700;0,800;1,400&family=Raleway:wght@300;400&display=swap" rel="stylesheet">
<style>
  :root{
    --red:#e3282a;
    --orange:#d8690f;
    --orange-dark:#c85a08;
    --navy:#1b2550;
    --blue-a:#1a3272;
    --blue-b:#2d69b6;
    --ink:#222;
    --grey-text:#444;
    --paper:#f1f1f3;
    --dark:#1a1a1c;
    --white:#fff;
  }
  html,body{margin:0;padding:0;overflow:hidden;}
  body{width:960px;height:1200px;background:#e9e9ea;}
  .flyer{position:relative;width:960px;height:1200px;overflow:hidden;background:var(--paper);
    font-family:"Montserrat",sans-serif;color:var(--ink);}
  .flyer-shapes{position:absolute;inset:0;width:960px;height:1200px;}
  .abs{position:absolute;}

  .hero-kicker{left:45px;top:408px;font-family:"Raleway",sans-serif;font-weight:300;font-size:34px;color:var(--white);letter-spacing:.5px;margin:0;line-height:1;}
  .hero-title{left:44px;top:446px;margin:0;font-weight:800;font-size:50px;line-height:54px;color:var(--red);}
  .hero-rule{left:50px;top:558px;width:80px;height:2px;background:var(--white);}
  .hero-text{left:51px;top:572px;width:350px;margin:0;font-family:"Raleway",sans-serif;font-size:13.5px;line-height:17.3px;color:#e6e6e6;}

  .call{left:58px;top:700px;width:600px;transform-origin:0 100%;transform:rotate(-21.5deg);color:var(--white);}
  .call-label{font-family:"Raleway",sans-serif;font-size:20px;letter-spacing:1px;margin:0 0 0 112px;}
  .call-number{font-weight:800;font-size:74px;line-height:1;margin:0;letter-spacing:1px;}
  .call{top:auto;bottom:288px;}

  .brand{left:548px;top:486px;width:150px;text-align:center;font-weight:700;font-size:19px;line-height:23px;color:#a9abb6;}
  .brand-mark{display:block;width:20px;height:20px;background:#b9bbc5;margin:0 auto 8px;}

  .features{left:290px;top:918px;width:650px;display:flex;margin:0;padding:0;list-style:none;}
  .feature{width:162px;text-align:center;}
  .feature svg{display:block;margin:0 auto 10px;}
  .feature-key{display:block;color:var(--orange);font-weight:800;font-size:16px;line-height:19px;}
  .feature-text{display:block;font-family:"Raleway",sans-serif;font-size:16px;line-height:20px;color:#222;}

  .about-title{right:44px;top:1024px;margin:0;font-family:"Raleway",sans-serif;font-weight:400;font-size:20px;color:var(--navy);}
  .about-title strong{font-family:"Montserrat",sans-serif;font-weight:800;color:#2560aa;}
  .about-text{right:44px;top:1052px;width:530px;margin:0;text-align:right;font-family:"Raleway",sans-serif;font-size:14.5px;line-height:20.8px;color:var(--grey-text);}

  .person{left:78px;top:960px;width:130px;height:130px;border-radius:50%;background:#d3d3d5;border:6px solid var(--white);box-shadow:0 2px 8px rgba(0,0,0,.25);}
  .person-name{left:47px;top:1097px;margin:0;font-weight:700;font-size:22px;color:var(--white);}
  .person-role{left:47px;top:1125px;margin:0;font-style:italic;font-size:16px;color:#fbe3cf;}

  .contact{top:1150px;height:50px;display:flex;align-items:center;color:var(--white);font-weight:600;font-size:20px;}
  .contact svg{margin-right:10px;}
  .contact-web{left:45px;}
  .contact-phone{left:390px;}
  .contact-mail{left:624px;}
</style>
</head>
<body>
<main class="flyer">
  <svg class="flyer-shapes" viewBox="90 65 1015 1330" preserveAspectRatio="none" aria-hidden="false">
    <defs>
      <linearGradient id="stoneWall" x1="0" y1="0" x2="1" y2="1">
        <stop offset="0" stop-color="#8f7a4f"/>
        <stop offset=".5" stop-color="#b39a66"/>
        <stop offset="1" stop-color="#7d6a48"/>
      </linearGradient>
      <linearGradient id="darkArch" x1="0" y1="0" x2="1" y2="1">
        <stop offset="0" stop-color="#232325"/>
        <stop offset="1" stop-color="#121213"/>
      </linearGradient>
      <linearGradient id="gateTone" x1="0" y1="0" x2="0" y2="1">
        <stop offset="0" stop-color="#9a9589"/>
        <stop offset="1" stop-color="#cfcbc2"/>
      </linearGradient>
      <linearGradient id="woodTone" x1="0" y1="0" x2="1" y2="1">
        <stop offset="0" stop-color="#6b5a49"/>
        <stop offset="1" stop-color="#8c7a66"/>
      </linearGradient>
      <linearGradient id="callBand" x1="0" y1="1" x2="1" y2="0">
        <stop offset="0" stop-color="var(--blue-a)"/>
        <stop offset=".6" stop-color="var(--blue-b)"/>
        <stop offset="1" stop-color="var(--blue-a)"/>
      </linearGradient>
      <linearGradient id="paperTone" x1="0" y1="0" x2="0" y2="1">
        <stop offset="0" stop-color="#f7f7f8"/>
        <stop offset="1" stop-color="#ececee"/>
      </linearGradient>
    </defs>

    <rect x="90" y="65" width="1015" height="1330" fill="url(#paperTone)"/>
    <polygon points="90,315 650,600 650,770 98,1000" fill="url(#darkArch)" role="img" aria-label="Dark photo of an arched doorway"/>
    <polygon points="90,65 1105,65 1105,465 885,575 740,495 595,575 90,315" fill="url(#stoneWall)" role="img" aria-label="Photo of a stone wall with arched wooden double doors"/>
    <polygon points="892,580 1105,468 1105,860 1030,822 892,742" fill="url(#gateTone)" role="img" aria-label="Photo of an iron gate detail"/>
    <polygon points="1035,830 1105,865 1105,1000 1035,985" fill="#e0e0e3"/>

    <polygon points="740,495 885,575 885,735 740,815 595,735 595,575" fill="#f3f3f5" stroke="#fff" stroke-width="8"/>
    <polygon points="880,745 1025,825 1025,985 880,1062 740,985 740,825" fill="url(#woodTone)" stroke="#fff" stroke-width="8" role="img" aria-label="Photo of a weathered wooden door with iron hardware"/>

    <polygon points="98,1000 728,744 745,820 100,1155" fill="url(#callBand)"/>

    <polygon points="100,1200 430,1200 480,1340 100,1340" fill="var(--orange)"/>
    <polygon points="100,1340 480,1340 455,1395 100,1395" fill="var(--orange-dark)"/>
    <polygon points="488,1340 1090,1340 1090,1395 462,1395" fill="var(--navy)"/>
  </svg>

  <section class="hero">
    <p class="abs hero-kicker">LOREM IPSUM</p>
    <h1 class="abs hero-title">IS SIMPLY<br>DUMMY TEXT</h1>
    <div class="abs hero-rule"></div>
    <p class="abs hero-text">Lorem Ipsum is simply dummy text of the printing and typesetting industry. Lorem Ipsum has been the industry's standard dummy text ever since the 1500s, Lorem Ipsum is simply dummy text of the printing and typesetting industry.</p>
  </section>

  <div class="abs brand"><span class="brand-mark"></span>Larkspur Panels and Spaces</div>

  <div class="abs call">
    <p class="call-label">PLEASE CALL US :</p>
    <p class="call-number">+0123 456 789</p>
  </div>

  <ul class="abs features">
    <li class="feature">
      <svg width="30" height="38" viewBox="0 0 30 38"><rect x="3" y="2" width="24" height="34" fill="none" stroke="#888" stroke-width="2"/><rect x="6" y="5" width="18" height="28" fill="#9b9b9e"/><circle cx="20" cy="19" r="1.6" fill="#fff"/></svg>
      <span class="feature-key">SIMPLY</span><span class="feature-text">DUMMY TEXT</span>
    </li>
    <li class="feature">
      <svg width="30" height="38" viewBox="0 0 30 38"><rect x="3" y="2" width="24" height="34" fill="none" stroke="#888" stroke-width="2"/><rect x="6" y="5" width="18" height="28" fill="#8d8d90"/><circle cx="20" cy="19" r="1.6" fill="#fff"/></svg>
      <span class="feature-key">SIMPLY</span><span class="feature-text">DUMMY TEXT</span>
    </li>
    <li class="feature">
      <svg width="30" height="38" viewBox="0 0 30 38"><rect x="3" y="2" width="24" height="34" fill="none" stroke="#888" stroke-width="2"/><polygon points="6,5 18,8 18,36 6,33" fill="#8d8d90"/></svg>
      <span class="feature-key">SIMPLY</span><span class="feature-text">DUMMY TEXT</span>
    </li>
    <li class="feature">
      <svg width="30" height="38" viewBox="0 0 30 38"><rect x="3" y="2" width="24" height="34" fill="none" stroke="#888" stroke-width="2"/><polygon points="6,5 15,8 15,34 6,33" fill="#9b9b9e"/></svg>
      <span class="feature-key">SIMPLY</span><span class="feature-text">DUMMY TEXT</span>
    </li>
  </ul>

  <h2 class="abs about-title">LOREM IPSUM IS <strong>SIMPLY DUMMY TEXT</strong></h2>
  <p class="abs about-text">Lorem Ipsum is simply dummy text of the printing and typesetting industry. Lorem Ipsum has been the industry's standard dummy text ever since the 1500s, when an unknown printer took a galley of type and scrambled it to make a type specimen book.</p>

  <div class="abs person" role="img" aria-label="Portrait photo of the contact person"></div>
  <p class="abs person-name">Name Goes Here</p>
  <p class="abs person-role">Designation Goes Here</p>

  <div class="abs contact contact-web">
    <svg width="20" height="20" viewBox="0 0 20 20" fill="none" stroke="#fff" stroke-width="1.5"><circle cx="10" cy="10" r="8"/><ellipse cx="10" cy="10" rx="3.5" ry="8"/><line x1="2" y1="10" x2="18" y2="10"/></svg>
    www.yourwebsite.com
  </div>
  <div class="abs contact contact-phone">
    <svg width="20" height="20" viewBox="0 0 20 20" fill="none" stroke="#fff" stroke-width="1.5"><circle cx="10" cy="10" r="8.5"/><path d="M8 5.5 L6.5 6.5 C6 9 8 13.5 11 14.5 L12.5 13.5 L11 11.5 L10 12 C9 11 8.5 10 8.4 8.8 L9.4 8.2 Z"/></svg>
    +0123 456 789
  </div>
  <div class="abs contact contact-mail">
    <svg width="34" height="22" viewBox="0 0 34 22" fill="none" stroke="#fff" stroke-width="1.5"><rect x="1" y="1" width="32" height="20"/><polyline points="1,1 17,13 33,1"/><line x1="1" y1="21" x2="13" y2="10"/><line x1="33" y1="21" x2="21" y2="10"/></svg>
    info@yourmailid.com
  </div>
</main>
</body>
</html>
```